Brand New Africa Focused Specialty Insurance business needs a slick website

Meridian Cover Partners needs a slick website design to launch our business with. we have 3 lines of business to begin with - Political Risk and Trade Credit and Property. (this will extend to 9: Political violence and Terrorism, Construction, Liability, Energy, Aviation, Marine, Parametric and Crisis Management at a later date). We are based in London but are Africa focused and our mission statement Meridian Cover Partners provides comprehensive, bespoke insurance risk mitigating solutions to local and global customers, giving them the confidence to grow their businesses sustainably. our tagline is "protecting Africa". Our colours are purple (Red 36, Green 11, Blue 96) and gold (Red 143, Green 137, Blue 53).

Target Market(s)

Brokers
Businesses across africa

Coding

Number of Pages Required

4 page

Font styles to use
Sans Serif
Other font styles liked:
• Cairo (but open to others too)

Requirements
Must have
• Pages:
1. Home page/about us (to include Lines of Business)
2. a page for Property line (we will need to add a link so that people can send an email to the mailbox)
3. a page for Political Risk and Trade Credit ( we will need to add a link so that people can send an email to the mailbox)
3. a page about our people (photos not yet taken for this)
4. a careers page
we have a lot of text for the above, we just need to fine tune it

must be tied to the colour scheme I detailed above.

the font for the logo is called Cairo
Nice to have
• https://www.tolvane-mu.com/ - we like the look of this website, but perhaps less colour
Should not have
• Any African animal like Lions or Zebras

```html
<!DOCTYPE html>
<html lang="en">
<head>
<meta charset="utf-8">
<title>Meridian Cover Partners — Protecting Africa</title>
<link href="https://fonts.googleapis.com/css2?family=Titillium+Web:wght@400;600;700&family=Open+Sans:ital,wght@0,400;0,600;1,400&display=swap" rel="stylesheet">
<style>
:root{
  --purple:#240b60;
  --gold:#8f8935;
  --gold-dark:#7d772c;
  --ink:#222;
  --muted:#555;
  --panel:#f3f3f3;
  --footer:#1c1c1c;
  --white:#fff;
}
*{margin:0;padding:0;box-sizing:border-box}
html,body{width:1200px;height:2997px;overflow:hidden;background:var(--white)}
body{position:relative;font-family:'Open Sans',sans-serif;color:var(--ink)}
.abs{position:absolute}
.head{font-family:'Titillium Web',sans-serif}

/* header */
.site-header{position:absolute;left:0;top:0;width:1200px;height:95px;background:var(--white)}
.brand{position:absolute;left:110px;top:6px;display:flex;align-items:center;gap:12px}
.brand-mark{width:84px;height:84px;border-radius:50%;border:2px solid var(--gold)}
.brand-name{font-family:'Titillium Web',sans-serif;font-weight:700;font-size:22px;color:var(--purple);line-height:1.1}
.brand-tag{font-family:'Titillium Web',sans-serif;font-weight:700;font-size:14px;color:var(--purple);margin-top:2px}
.main-nav{position:absolute;right:112px;top:38px;display:flex;gap:21px;font-family:'Titillium Web',sans-serif;font-size:19px;color:#333}

/* hero */
.hero{position:absolute;left:0;top:95px;width:1200px;height:522px;
  background:linear-gradient(100deg,#f4f4f4 0%,#eceeef 45%,#d9d5cf 70%,#e6e8ea 100%)}
.hero-title{position:absolute;left:107px;top:95px;font-family:'Titillium Web',sans-serif;font-weight:700;font-size:74px;line-height:84px;color:#2a2a2a}
.btn-gold{position:absolute;left:112px;top:281px;width:303px;height:64px;background:var(--gold);color:var(--white);
  font-family:'Titillium Web',sans-serif;font-weight:700;font-size:21px;display:flex;align-items:center;justify-content:center;border-radius:2px}

/* mission */
.mission{position:absolute;left:0;top:617px;width:1200px;height:264px;background:var(--purple);color:var(--white);text-align:center}
.mission h2{font-family:'Titillium Web',sans-serif;font-weight:700;font-size:44px;margin-top:34px}
.mission p{font-size:18.5px;font-weight:600;line-height:34px;width:900px;margin:12px auto 0}
.line-item{position:absolute;top:812px;width:206px;text-align:center;margin-left:-103px}
.line-ring{width:206px;height:206px;border-radius:50%;background:var(--white);display:flex;align-items:center;justify-content:center}
.line-circle{width:178px;height:178px;border-radius:50%;border:3px solid var(--gold);display:flex;align-items:center;justify-content:center}
.line-label{font-family:'Titillium Web',sans-serif;font-weight:700;font-size:28px;color:#333;margin-top:6px}

/* about */
.about-panel{position:absolute;left:112px;top:1113px;width:410px;height:367px;background:var(--panel);padding:30px 36px}
.about-panel h3{font-family:'Titillium Web',sans-serif;font-weight:700;font-size:42px;line-height:53px;color:#222}
.about-panel p{font-size:15.5px;line-height:29px;color:#555;margin-top:16px}
.link-gold{font-family:'Titillium Web',sans-serif;font-weight:700;font-size:17px;color:var(--gold);letter-spacing:.3px}
.about-media{position:absolute;left:522px;top:1113px;width:566px;height:367px;
  background:linear-gradient(120deg,#d8cfc4 0%,#b79a80 35%,#6f6a62 60%,#d9d8d4 100%)}
.play{position:absolute;left:254px;top:154px;width:58px;height:58px;border-radius:50%;background:#1f1f1f;display:flex;align-items:center;justify-content:center}

/* testimonials */
.testimonials{position:absolute;left:0;top:1537px;width:1200px;height:466px;background:var(--gold);overflow:hidden}
.testimonials .ring{position:absolute;left:100px;top:-140px;width:1000px;height:760px;border-radius:50%;border:14px solid rgba(255,255,255,.08)}
.testimonials h2{position:absolute;left:0;width:1200px;top:49px;text-align:center;font-family:'Titillium Web',sans-serif;font-weight:700;font-size:44px;color:var(--white)}
.quote-card{position:absolute;top:133px;width:307px;height:262px;border:2px solid rgba(255,255,255,.55);padding:22px 16px;color:var(--white)}
.quote-card p{font-style:italic;font-size:16px;line-height:27.5px}
.quote-author{display:flex;align-items:center;gap:18px;margin:14px 0 0 40px}
.avatar{width:96px;height:96px;border-radius:50%;background:#d0d0d0;flex:none}
.author-name{font-family:'Titillium Web',sans-serif;font-size:21px;line-height:24px}
.author-role{font-family:'Titillium Web',sans-serif;font-size:17px;line-height:22px}
.arrow{position:absolute;top:244px}

/* careers */
.careers-title{position:absolute;left:0;width:1200px;top:2050px;text-align:center;font-family:'Titillium Web',sans-serif;font-weight:700;font-size:44px;color:#222}
.feature-card{position:absolute;left:112px;top:2133px;width:471px;height:420px;background:var(--white);box-shadow:0 2px 14px rgba(0,0,0,.12)}
.feature-img{width:471px;height:229px;background:linear-gradient(160deg,#e9eaec 0%,#c9c7c4 50%,#8c8a88 100%)}
.post-title{font-family:'Titillium Web',sans-serif;font-size:23px;color:#222}
.meta{font-size:15px;color:#666;display:flex;align-items:center;gap:6px;margin-top:6px}
.post-text{font-size:15.5px;line-height:27px;color:#555;margin-top:8px}
.feature-body{padding:18px 22px}
.post-item{position:absolute;left:612px;width:480px;height:161px}
.post-thumb{position:absolute;left:0;top:0;width:189px;height:161px}
.post-info{position:absolute;left:212px;top:0;width:270px}

/* footer */
.site-footer{position:absolute;left:0;top:2616px;width:1200px;height:381px;background:var(--footer);color:var(--white)}
.footer-brand{position:absolute;left:90px;top:144px;display:flex;align-items:center;gap:12px}
.footer-brand .brand-mark{width:92px;height:92px;border-color:var(--white)}
.footer-brand .brand-name{color:var(--white);font-size:25px}
.footer-brand .brand-tag{color:var(--white);font-size:16px}
.foot-col{position:absolute;top:50px}
.foot-col h4{font-family:'Titillium Web',sans-serif;font-weight:700;font-size:17px;margin-bottom:8px}
.foot-col li{list-style:none;font-size:14.5px;line-height:27px}
.contact-row{display:flex;gap:10px;font-size:15.5px;line-height:27px}
.divider{position:absolute;left:110px;top:286px;width:978px;height:1px;background:#555}
.copyright{position:absolute;left:110px;top:318px;font-size:15.5px}
.social{position:absolute;top:307px;width:43px;height:43px;border-radius:50%;border:1px solid #bbb}
</style>
</head>
<body>

<header class="site-header">
  <div class="brand">
    <div class="brand-mark"></div>
    <div>
      <div class="brand-name">Meridian Cover Partners</div>
      <div class="brand-tag">Protecting Africa</div>
    </div>
  </div>
  <nav class="main-nav">
    <span>About us</span><span>Property Line</span><span>Political Risk</span><span>Trade Credit</span><span>Our People</span><span>Careers</span>
  </nav>
</header>

<section class="hero" role="img" aria-label="Photo of hands reviewing financial charts at a desk with a laptop">
  <h1 class="hero-title">Protecting<br>Africa</h1>
  <div class="btn-gold">REQUEST A CONSULTATION</div>
</section>

<section class="mission">
  <h2>Our Mission</h2>
  <p>Meridian Cover Partners provides comprehensive, bespoke insurance risk mitigating solutions to local and global customers, giving them the confidence to grow their businesses sustainably.</p>
</section>

<div class="line-item" style="left:269px">
  <div class="line-ring"><div class="line-circle">
    <svg width="74" height="68" viewBox="0 0 74 68"><path d="M37 2 L72 66 H2 Z" fill="var(--gold)"/><rect x="32" y="22" width="10" height="24" fill="#fff"/><rect x="32" y="51" width="10" height="9" fill="#fff"/></svg>
  </div></div>
  <div class="line-label">Political Risk</div>
</div>
<div class="line-item" style="left:600px">
  <div class="line-ring"><div class="line-circle">
    <svg width="84" height="64" viewBox="0 0 84 64"><path d="M3 2 V60 H82" stroke="var(--gold)" stroke-width="5" fill="none"/><path d="M12 50 L30 30 L44 40 L62 20 L70 26 L78 10 L60 12" stroke="var(--gold)" stroke-width="6" fill="none" stroke-linejoin="round"/><path d="M12 52 L30 32 L44 42 L66 18 L78 10 V54 H12Z" fill="var(--gold)"/></svg>
  </div></div>
  <div class="line-label">Trade Credit</div>
</div>
<div class="line-item" style="left:941px">
  <div class="line-ring"><div class="line-circle">
    <svg width="56" height="72" viewBox="0 0 56 72"><rect x="2" y="2" width="52" height="68" fill="var(--gold)"/><g fill="#fff"><rect x="9" y="9" width="6" height="6"/><rect x="19" y="9" width="6" height="6"/><rect x="29" y="9" width="6" height="6"/><rect x="39" y="9" width="6" height="6"/><rect x="9" y="20" width="6" height="6"/><rect x="19" y="20" width="6" height="6"/><rect x="29" y="20" width="6" height="6"/><rect x="39" y="20" width="6" height="6"/><rect x="9" y="31" width="6" height="6"/><rect x="19" y="31" width="6" height="6"/><rect x="29" y="31" width="6" height="6"/><rect x="39" y="31" width="6" height="6"/><rect x="9" y="42" width="6" height="6"/><rect x="39" y="42" width="6" height="6"/><rect x="22" y="52" width="12" height="18"/></g></svg>
  </div></div>
  <div class="line-label">Property</div>
</div>

<section>
  <div class="about-panel">
    <h3>Meridian Cover Partners</h3>
    <p>Nemo enim ipsam voluptatem quia voluptas sit aspernatur aut odit aut fugit, sed quia cons equuntur magni dolores eos qui ratione volup tatem sequi nesciunt. Neque porro quisquam est, qui dolorem ipsum quia</p>
    <div class="link-gold" style="margin-top:18px">ABOUT US</div>
  </div>
  <div class="about-media" role="img" aria-label="Video still of three colleagues smiling while reviewing documents at a table">
    <div class="play"><svg width="22" height="24" viewBox="0 0 22 24"><path d="M2 1 L21 12 L2 23Z" fill="#fff"/></svg></div>
  </div>
</section>

<section class="testimonials">
  <div class="ring"></div>
  <h2>Client Testimonials</h2>
  <svg class="arrow" style="left:66px" width="18" height="30" viewBox="0 0 18 30"><path d="M15 2 L3 15 L15 28" stroke="#fff" stroke-width="3" fill="none" opacity=".8"/></svg>
  <svg class="arrow" style="left:1104px" width="18" height="30" viewBox="0 0 18 30"><path d="M3 2 L15 15 L3 28" stroke="#fff" stroke-width="3" fill="none" opacity=".8"/></svg>
  <div class="quote-card" style="left:112px">
    <p>“Nam libero tempore, cum soluta nobis est eligendi opticum que nihil impedit quo minus id quod maxime placeat facere possimus”</p>
    <div class="quote-author"><div class="avatar"></div><div><div class="author-name">Amara Bello</div><div class="author-role">CEO</div></div></div>
  </div>
  <div class="quote-card" style="left:447px">
    <p>“Nam libero tempore, cum soluta nobis est eligendi opticum que nihil impedit quo minus id quod maxime placeat facere possimus”</p>
    <div class="quote-author"><div class="avatar"></div><div><div class="author-name">Amara Bello</div><div class="author-role">CEO</div></div></div>
  </div>
  <div class="quote-card" style="left:781px">
    <p>“Nam libero tempore, cum soluta nobis est eligendi opticum que nihil impedit quo minus id quod maxime placeat facere possimus”</p>
    <div class="quote-author"><div class="avatar"></div><div><div class="author-name">Amara Bello</div><div class="author-role">CEO</div></div></div>
  </div>
</section>

<section>
  <h2 class="careers-title">Careers</h2>
  <article class="feature-card">
    <div class="feature-img" role="img" aria-label="Photo of a hand using a calculator beside a laptop and glasses"></div>
    <div class="feature-body">
      <div class="post-title">Finibus Bonorum et Malorum</div>
      <div class="meta">
        <svg width="13" height="13" viewBox="0 0 13 13"><rect x="1" y="2" width="11" height="10" fill="none" stroke="var(--purple)" stroke-width="1.6"/><rect x="1" y="2" width="11" height="3" fill="var(--purple)"/></svg>
        10/09/2020 &nbsp;| &nbsp;
        <svg width="12" height="13" viewBox="0 0 12 13"><circle cx="6" cy="3.5" r="3" fill="var(--purple)"/><path d="M0 13 Q6 4 12 13Z" fill="var(--purple)"/></svg>
        Amara Bello
      </div>
      <p class="post-text">Nemo enim ipsam voluptatem quia voluptas sit aspernatur aut odit aut fugit, sed quia consequuntu.</p>
      <div class="link-gold" style="margin-top:8px;font-size:16px">READ MORE</div>
    </div>
  </article>

  <article class="post-item" style="top:2133px">
    <div class="post-thumb" role="img" aria-label="Photo of two colleagues looking at a tablet in an office" style="background:linear-gradient(135deg,#cfd2d4,#5a5650 60%,#9a9894)"></div>
    <div class="post-info">
      <div class="post-title" style="font-size:22px">Finibus Bonorum et Malorum</div>
      <div class="meta">
        <svg width="13" height="13" viewBox="0 0 13 13"><rect x="1" y="2" width="11" height="10" fill="none" stroke="var(--purple)" stroke-width="1.6"/><rect x="1" y="2" width="11" height="3" fill="var(--purple)"/></svg>
        10/09/2020 &nbsp;| &nbsp;
        <svg width="12" height="13" viewBox="0 0 12 13"><circle cx="6" cy="3.5" r="3" fill="var(--purple)"/><path d="M0 13 Q6 4 12 13Z" fill="var(--purple)"/></svg>
        Amara Bello
      </div>
      <p class="post-text" style="line-height:27px">Nemo enim ipsam voluptatem quia voluptas sit aspernatu</p>
      <div class="link-gold" style="margin-top:6px;font-size:16px">READ MORE</div>
    </div>
  </article>

  <article class="post-item" style="top:2322px">
    <div class="post-thumb" role="img" aria-label="Photo of a man on a phone call at his desk" style="background:linear-gradient(135deg,#e8e4dc,#8a6a54 50%,#3e5d80)"></div>
    <div class="post-info">
      <div class="post-title" style="font-size:22px">Finibus Bonorum et Malorum</div>
      <div class="meta">
        <svg width="13" height="13" viewBox="0 0 13 13"><rect x="1" y="2" width="11" height="10" fill="none" stroke="var(--purple)" stroke-width="1.6"/><rect x="1" y="2" width="11" height="3" fill="var(--purple)"/></svg>
        10/09/2020 &nbsp;| &nbsp;
        <svg width="12" height="13" viewBox="0 0 12 13"><circle cx="6" cy="3.5" r="3" fill="var(--purple)"/><path d="M0 13 Q6 4 12 13Z" fill="var(--purple)"/></svg>
        Amara Bello
      </div>
      <p class="post-text">Nemo enim ipsam voluptatem quia voluptas sit aspernatu</p>
      <div class="link-gold" style="margin-top:6px;font-size:16px">READ MORE</div>
    </div>
  </article>

  <div class="abs link-gold" style="left:610px;top:2514px;font-size:18px">VIEW MORE</div>
</section>

<footer class="site-footer">
  <div class="footer-brand">
    <div class="brand-mark"></div>
    <div>
      <div class="brand-name">Meridian Cover Partners</div>
      <div class="brand-tag">Protecting Africa</div>
    </div>
  </div>
  <div class="foot-col" style="left:486px">
    <h4>Information</h4>
    <ul><li>About us</li><li>Property Line</li><li>Political Risk</li><li>Trade Credit</li><li>Our People</li><li>Careers</li></ul>
  </div>
  <div class="foot-col" style="left:665px">
    <h4>Quick Links</h4>
    <ul><li>Sitemap</li><li>Insights</li><li>Privacy Policy</li></ul>
  </div>
  <div class="foot-col" style="left:850px">
    <h4>Find Us</h4>
    <div class="contact-row"><svg width="10" height="15" viewBox="0 0 10 15" style="margin-top:6px"><path d="M5 0 A5 5 0 0 1 10 5 C10 9 5 15 5 15 C5 15 0 9 0 5 A5 5 0 0 1 5 0Z" fill="#fff"/><circle cx="5" cy="5" r="2" fill="var(--footer)"/></svg><span>12 Rue de Corvell Ouest<br>75008 Africa</span></div>
    <div class="contact-row" style="margin-top:27px"><svg width="14" height="14" viewBox="0 0 14 14" style="margin-top:6px"><path d="M3 0 L6 3 L4 5 Q6 8 9 10 L11 8 L14 11 L12 14 Q4 13 0 3Z" fill="#fff"/></svg><span>1 800 555 0142</span></div>
    <div class="contact-row" style="margin-top:27px"><svg width="17" height="13" viewBox="0 0 17 13" style="margin-top:7px"><rect width="17" height="13" rx="1" fill="#fff"/><path d="M1 1 L8.5 7 L16 1" stroke="var(--footer)" stroke-width="1.5" fill="none"/></svg><span>info@meridiancover.example</span></div>
  </div>
  <div class="divider"></div>
  <div class="copyright">© 2020, Meridian Cover Partners.</div>
  <div class="social" style="left:945px"></div>
  <div class="social" style="left:993px"></div>
  <div class="social" style="left:1044px"></div>
</footer>

</body>
</html>
```